Amber Hollow Productions

I need a business card design for a new freelance film production company using or incorporating the logo:
I want the card to be creative, minimal, yet professional. Feel free to use a variety of different shapes and sizes/ textures for the card.

Industry/Entity Type

Film Production

```html
<!DOCTYPE html>
<html lang="en">
<head>
<meta charset="utf-8">
<title>Amber Hollow Productions – Business Card</title>
<link href="https://fonts.googleapis.com/css2?family=Source+Sans+3:wght@400;600;700&display=swap" rel="stylesheet">
<style>
  :root {
    --brand-blue: #1558a6;
    --paper: #ffffff;
    --backdrop: #ffffff;
  }
  html, body {
    margin: 0;
    padding: 0;
    overflow: hidden;
    background: var(--backdrop);
  }
  .canvas {
    position: relative;
    width: 1200px;
    height: 848px;
    overflow: hidden;
    background: var(--backdrop);
    font-family: "Source Sans 3", "Myriad Pro", Arial, sans-serif;
  }
  .card {
    position: absolute;
    width: 364px;
    height: 222px;
    overflow: hidden;
  }
  .card--back {
    left: 181px;
    top: 307px;
    background: var(--brand-blue);
  }
  .card--front {
    left: 648px;
    top: 309px;
    background: var(--paper);
    box-shadow: 3px 5px 8px rgba(0, 0, 0, 0.22);
  }
  .film-strip {
    position: absolute;
    left: 0;
    width: 364px;
    display: block;
  }
  .film-strip--top { top: 0; }
  .film-strip--bottom { bottom: 0; }
  .divider-line {
    position: absolute;
    left: 0;
    top: 15px;
    width: 364px;
    height: 4px;
    background: var(--paper);
  }
  .emblem {
    position: absolute;
    left: 99px;
    top: 30px;
    width: 156px;
    height: 156px;
    border-radius: 50%;
    display: flex;
    align-items: center;
    justify-content: center;
    text-align: center;
  }
  .card--back .emblem { left: 99px; top: 30px; background: var(--paper); }
  .card--front .emblem { left: 94px; top: 28px; background: var(--brand-blue); }
  .emblem__name {
    font-weight: 600;
    font-size: 16px;
    line-height: 1.15;
    letter-spacing: 0.04em;
    text-transform: uppercase;
    width: 120px;
  }
  .card--back .emblem__name { color: var(--brand-blue); }
  .card--front .emblem__name { color: var(--paper); }
  .web-address {
    position: absolute;
    left: 0;
    width: 364px;
    top: 191px;
    text-align: center;
    color: var(--paper);
    font-size: 12.5px;
    letter-spacing: 0.01em;
    white-space: nowrap;
  }
  .contact-row {
    position: absolute;
    left: 16px;
    right: 15px;
    top: 184px;
    display: flex;
    justify-content: space-between;
    color: var(--brand-blue);
    font-weight: 700;
    font-size: 13px;
    white-space: nowrap;
  }
</style>
</head>
<body>
<div class="canvas">

  <svg width="0" height="0" style="position:absolute" aria-hidden="true">
    <defs>
      <pattern id="sprocket-holes" x="11" y="0" width="21.3" height="16" patternUnits="userSpaceOnUse">
        <rect x="0" y="5" width="10" height="6" fill="#ffffff"/>
      </pattern>
    </defs>
  </svg>

  <section class="card card--back" aria-label="Card back">
    <svg class="film-strip film-strip--top" width="364" height="15" viewBox="0 0 364 15">
      <rect width="364" height="15" fill="#1558a6"/>
      <rect x="0" y="-1" width="364" height="16" fill="url(#sprocket-holes)"/>
    </svg>
    <div class="divider-line"></div>
    <div class="emblem">
      <span class="emblem__name">Amber Hollow Productions</span>
    </div>
    <p class="web-address" style="margin:0">WWW . AMBER HOLLOW PRODUCTIONS . COM</p>
    <svg class="film-strip film-strip--bottom" width="364" height="15" viewBox="0 0 364 15">
      <rect width="364" height="15" fill="#1558a6"/>
      <rect x="0" y="1" width="364" height="16" fill="url(#sprocket-holes)"/>
    </svg>
  </section>

  <section class="card card--front" aria-label="Card front">
    <svg class="film-strip film-strip--top" width="364" height="14" viewBox="0 0 364 14">
      <rect width="364" height="14" fill="#1558a6"/>
      <rect x="0" y="-2" width="364" height="16" fill="url(#sprocket-holes)"/>
    </svg>
    <div class="emblem">
      <span class="emblem__name">Amber Hollow Productions</span>
    </div>
    <div class="contact-row">
      <span class="contact-row__name">MARA QUILL</span>
      <span class="contact-row__email">E: mara@amberhollow.com</span>
      <span class="contact-row__phone">T: 9472 3186</span>
    </div>
    <svg class="film-strip film-strip--bottom" width="364" height="16" viewBox="0 0 364 16">
      <rect width="364" height="16" fill="#1558a6"/>
      <rect x="0" y="0" width="364" height="16" fill="url(#sprocket-holes)"/>
    </svg>
  </section>

</div>
</body>
</html>
```